Etiketten-Design für Gin- und Rumhersteller
Zielgruppe
Zielgruppe 20-35 Jahre, Wir sind ein Gin- und Rumhersteller und hätten gerne ein Etikett für unsere Flaschen. Etikett-Maße jeweils 70 x 70 mm.
Aufgabenstellung
Schwarzweißes Design, eventuell mit Gold oder Silber, Etikett selbst schwarz. Junger moderner Stil, Das Logo soll Groß auf dem Etikett sichtbar sein. Es gibt nur eine Vorderseite. Maße 70 x 70 mm.
Etikett Aufbau :
Wolkenhof (Groß, Logo anbei)
GIN oder RUM
40% Alk
hergestellt & abgefüllt in Vorarlberg
Wolkenhof Gin
aus der Firmengruppe der
HausKontor (Klein, Logo anbei)

```html
<!DOCTYPE html>
<html lang="de">
<head>
<meta charset="utf-8">
<title>Wolkenhof Gin – Etikett</title>
<link rel="stylesheet" href="https://fonts.googleapis.com/css2?family=Montserrat:wght@200;400&family=Roboto+Condensed:wght@300;400;700&display=swap">
<style>
  :root {
    --stage: #0c0c0d;
    --label-dark: #1b1d28;
    --label-mid: #23263a;
    --ink: #ffffff;
    --ink-soft: #e9e9ee;
    --gold: #d7b36a;
    --gold-light: #f3dc9c;
    --gold-deep: #a9813c;
    --botanical: rgba(255,255,255,0.045);
  }
  * { margin: 0; padding: 0; box-sizing: border-box; }
  html, body {
    width: 1091px; height: 1200px; overflow: hidden;
    background: var(--stage);
  }
  .label {
    position: absolute; left: 115px; top: 170px;
    width: 860px; height: 860px;
    background: linear-gradient(90deg, var(--label-dark) 0%, var(--label-mid) 45%, var(--label-dark) 100%);
    overflow: hidden;
  }
  .brand-name {
    position: absolute; left: 140px; top: 444px;
    transform: translate(-50%, -50%) rotate(-90deg);
    font-family: "Montserrat", sans-serif; font-weight: 400;
    font-size: 118px; letter-spacing: 4px; line-height: 1;
    color: var(--ink); white-space: nowrap;
  }
  .botanical {
    position: absolute; left: 251px; top: 96px;
    width: 420px; height: 614px;
    background: radial-gradient(ellipse at 50% 50%, var(--botanical) 0%, rgba(255,255,255,0) 70%);
  }
  .rule {
    position: absolute; height: 3px;
    background: linear-gradient(90deg, var(--gold-deep), var(--gold-light) 50%, var(--gold-deep));
  }
  .rule--top { left: 267px; top: 76px; width: 473px; }
  .rule--mid { left: 281px; top: 436px; width: 405px; }
  .rule--low { left: 281px; top: 644px; width: 466px; }
  .product {
    position: absolute; left: 270px; top: 136px;
    font-family: "Montserrat", sans-serif; font-weight: 200;
    font-size: 232px; line-height: 1; letter-spacing: 58px;
    color: var(--ink);
  }
  .seal { position: absolute; left: 679px; top: 386px; width: 148px; height: 148px; }
  .origin {
    position: absolute; left: 281px; top: 572px; width: 466px;
    font-family: "Roboto Condensed", sans-serif; font-weight: 400;
    font-size: 34px; letter-spacing: 0.6px; text-align: center;
    color: var(--ink-soft); white-space: nowrap;
  }
  .group-note {
    position: absolute; left: 277px; top: 736px;
    font-family: "Roboto Condensed", sans-serif; font-weight: 300;
    font-size: 20px; color: var(--ink-soft);
  }
  .group-name {
    position: absolute; left: 277px; top: 766px;
    font-family: "Roboto Condensed", sans-serif; font-weight: 700;
    font-size: 33px; line-height: 1; color: var(--ink);
  }
  .strength {
    position: absolute; right: 111px; top: 752px;
    font-family: "Montserrat", sans-serif; font-weight: 400;
    font-size: 54px; line-height: 1; color: var(--ink);
  }
  .strength small { font-size: 32px; margin-left: 8px; }
</style>
</head>
<body>
  <section class="label" aria-label="Flaschenetikett Wolkenhof Gin">
    <div class="botanical" role="img" aria-label="Dezente Wacholderzweig-Illustration im Hintergrund"></div>
    <div class="brand-name">Wolkenhof</div>
    <div class="rule rule--top"></div>
    <h1 class="product">GIN</h1>
    <div class="rule rule--mid"></div>
    <svg class="seal" viewBox="0 0 148 148" role="img" aria-label="Goldsiegel">
      <defs>
        <radialGradient id="sealFill" cx="40%" cy="35%" r="70%">
          <stop offset="0%" stop-color="#fbeec4"/>
          <stop offset="60%" stop-color="#e2c07a"/>
          <stop offset="100%" stop-color="#b48a43"/>
        </radialGradient>
      </defs>
      <circle cx="74" cy="74" r="72" fill="url(#sealFill)"/>
    </svg>
    <p class="origin">Hergestellt &amp; abgefüllt in Vorarlberg</p>
    <div class="rule rule--low"></div>
    <p class="group-note">Aus der Firmengruppe der</p>
    <p class="group-name">HausKontor</p>
    <p class="strength">40%<small>Alk</small></p>
  </section>
</body>
</html>
```